Redesign of ormavue.com website (3 page types)

We need a fresh rebrush of www.ormavue.com, a portal for french regions, departements and cities. It shall look modern as the current design is over 10 years old.

We like the blueish colors and the french touch (blue, white, red).

There are 3 page types that we currently need:
- Homepage (http://www.ormavue.com/)
- Region overview (e.g. http://www.ormavue.com/provence-alpes-cote-d-azur)
- City overview (e.g. http://www.ormavue.com/provence-alpes-cote-d-azur/bouches-du-rhone/marseille)

See "Must have" for a more detailed briefing. All required elements exist and need a rebrush/redesign

Requirements
Must have
• General:

- 3 column layout
+ Header
+ Left sidebar
+ Content area
+ Right sidebar (250px inner width for ads)
+ Footer
- 3 classes of headlines
- Simple sidebar widgets (headline & content / without headline)

Header:
- Logo
- 2 or 3 links
- Search box
- Breadcrumb navigation

Footer:
- Nothing special, really

Homepage:
- Nice looking map with visible region borders to create a mouseover effect (as seen on current version). Meaning we need the plain map and a version with each region highlighted
- Text areas
- Content boxes (like the current gray ones)

Region overview
- Headline
- Info box (Informations)
- Mini map
- Crest / emblem
- Text area with headline for a long descriptive text with a "read more" / "show less" button/link to pop out the whole text via javascript
- List of the 24 biggest cities in the region

City overview
- Headline
- Info box (Informations, same look as for regions)
- Mini map
- List of the 24 cities nearby
- List of available photos
- Example sidebar widgets (right sidebar):
+ Upload a photo of this city
+ Weather conditions
+ Link list
Nice to have
• - A new favicon
- Pindora og:image
Should not have
• - Flash
- Animations

```html
<!DOCTYPE html>
<html lang="fr">
<head>
<meta charset="utf-8">
<title>Marseille – ormavue</title>
<link rel="stylesheet" href="https://fonts.googleapis.com/css2?family=Open+Sans:ital,wght@0,400;0,600;0,700;1,400;1,600&display=swap">
<style>
:root{
  --blue:#2f6090;
  --blue-dark:#28557f;
  --blue-light:#c9def2;
  --link:#2d5f95;
  --red:#7a1517;
  --page:#f4fbfb;
  --text:#333b44;
  --muted:#5b6570;
  --line:#dfe6ea;
  --sun:#e1a044;
}
*{box-sizing:border-box;margin:0;padding:0}
html,body{width:698px;height:1200px;overflow:hidden}
body{font-family:"Open Sans",Arial,sans-serif;background:var(--page);color:var(--text);position:relative}
a{color:var(--link);text-decoration:none}
.abs{position:absolute}

/* header */
.site-header{position:absolute;left:0;top:0;width:698px;height:44px;background:var(--page)}
.brand{position:absolute;left:38px;top:0;width:116px;height:64px;background:#fff;z-index:3;display:flex;align-items:center;justify-content:center;gap:5px}
.brand-mark{width:9px;height:9px;background:var(--red)}
.brand-name{font-weight:700;font-size:17px;color:var(--blue)}
.main-nav{position:absolute;left:244px;top:14px;display:flex;gap:0}
.main-nav a{font-size:9.5px;color:#3b434b;height:16px;line-height:16px;padding:0 5px;margin-right:9px}
.main-nav a.current{background:var(--blue);color:#fff;border-radius:2px}
.search-band{position:absolute;left:521px;top:0;width:177px;height:44px;background:var(--red)}
.search-box{position:absolute;left:13px;top:14px;width:113px;height:18px;background:#fff;border:1px solid #bbb;font-size:8.5px;font-style:italic;color:#999;padding:2px 6px}
.search-box svg{position:absolute;right:5px;top:4px}

/* hero */
.hero{position:absolute;left:0;top:44px;width:698px;height:169px;background:linear-gradient(100deg,#1d4f9d 0%,#2a5fb0 40%,#b8a28d 62%,#c88a66 100%)}
.hero-title{position:absolute;left:49px;top:110px;font-size:30px;font-weight:700;color:#fff;text-shadow:0 1px 3px rgba(0,0,0,.4)}
.hero-dots{position:absolute;left:326px;top:153px;display:flex;gap:6px}
.hero-dots span{width:6px;height:6px;border-radius:50%;background:rgba(255,255,255,.55)}
.hero-dots span:first-child{background:#fff}
.mini-map{position:absolute;left:402px;top:182px;width:80px;height:100px;background:var(--blue);border:3px solid #fff;border-radius:40% 45% 35% 50%;z-index:2}

/* left nav */
.side-nav{position:absolute;left:38px;top:231px;width:140px;height:115px;background:var(--blue-light);font-size:9px}
.side-nav a{position:absolute;left:13px;color:#444}
.side-nav hr{position:absolute;left:0;top:57px;width:140px;border:0;border-top:1px solid #fff}
.side-nav a.current{color:var(--link);text-decoration:underline}

/* content */
.section-title{font-size:11.5px;font-weight:700;color:var(--blue)}
.info-table{position:absolute;left:203px;top:260px;font-size:8.8px;border-collapse:collapse}
.info-table th{font-weight:400;color:var(--muted);text-align:left;width:92px;height:15.2px;padding:0}
.info-table td{color:#222;padding:0}
.tourism{position:absolute;left:203px;top:436px;width:282px;font-size:8.4px;line-height:15.2px;color:#444}
.more{position:absolute;left:417px;top:578px;font-size:8.8px;font-style:italic;font-weight:600;color:var(--link)}

/* right sidebar */
.widget-upload{position:absolute;left:502px;top:232px;width:158px;height:46px;background:var(--blue);color:#fff;font-size:10px;font-weight:700;text-align:center;line-height:15.5px;padding-top:8px}
.widget-head{position:absolute;left:502px;width:158px;height:29px;background:var(--blue);color:#fff;font-size:10px;font-weight:700;padding:7px 13px;border-bottom:1px solid #9fb9d2}
.widget-body{position:absolute;left:502px;width:158px;background:var(--blue-light);font-size:8.6px;color:#333}

/* lower panel */
.lower{position:absolute;left:38px;top:617px;width:622px;height:303px;background:#fff0;border:1px solid var(--line)}
.lower-divider{position:absolute;left:304px;top:0;width:1px;height:301px;background:var(--line)}
.nearby{position:absolute;left:13px;top:50px;display:grid;grid-template-columns:91px 62px 91px 40px;grid-auto-rows:22.9px;font-size:8.4px;grid-auto-flow:column;grid-template-rows:repeat(11,22.9px)}
.nearby .d{color:#333}
.photos{position:absolute;left:317px;top:46px;display:grid;grid-template-columns:repeat(4,63px);grid-auto-rows:63px;gap:13px 13.5px}
.photos div{background:var(--blue-light);border:1px solid #b9c9d7}

/* footer */
.site-footer{position:absolute;left:0;top:978px;width:698px;height:222px;background:linear-gradient(180deg,#2f6090,#3c6f9c);color:#fff;font-size:8.8px}
.footer-brand{position:absolute;left:50px;top:20px;display:flex;align-items:center;gap:5px;font-weight:700;font-size:16px}
.footer-brand span{width:8px;height:8px;background:#fff}
.footer-links a,.city-links a{position:absolute;color:#fff}
.foot-title{position:absolute;top:36px;font-size:10px;font-weight:600;letter-spacing:.2px}
.news{position:absolute;left:356px;top:57px;width:145px;line-height:11.5px}
.foot-photos{position:absolute;left:508px;top:57px;display:grid;grid-template-columns:repeat(3,38px);gap:13px 12px}
.foot-photos div{height:38px;border:1px solid #fff}
</style>
</head>
<body>

<header class="site-header">
  <div class="brand"><span class="brand-mark"></span><span class="brand-name">ormavue</span></div>
  <nav class="main-nav">
    <a class="current" href="#">HOME</a><a href="#">ARCHIVES</a><a href="#">ABOUT</a><a href="#">CONTACT</a>
  </nav>
  <div class="search-band">
    <div class="search-box">Recherche
      <svg width="8" height="8" viewBox="0 0 8 8"><circle cx="3.2" cy="3.2" r="2.4" fill="none" stroke="#999" stroke-width="1"/><path d="M5 5l2.5 2.5" stroke="#999" stroke-width="1"/></svg>
    </div>
  </div>
</header>

<section class="hero" role="img" aria-label="Vue aérienne d'une baie méditerranéenne et de la ville en bord de mer">
  <h1 class="hero-title">Marseille</h1>
  <div class="hero-dots"><span></span><span></span><span></span><span></span></div>
</section>
<div class="mini-map" role="img" aria-label="Carte de France avec la région de Marseille mise en évidence"></div>

<nav class="side-nav">
  <a href="#" style="top:18px">Accueil</a>
  <a href="#" style="top:37px">Aperçu Marseille</a>
  <hr>
  <a href="#" class="current" style="top:75px">Météo</a>
  <a href="#" style="top:94px">Carte</a>
</nav>

<h2 class="section-title abs" style="left:203px;top:230px">Informations</h2>
<table class="info-table">
  <tr><th>Nombre d'habitants:</th><td>826,700</td></tr>
  <tr><th>Région:</th><td><a href="#">Provence-Alpes-Côte d'Azur</a></td></tr>
  <tr><th>Departements:</th><td><a href="#">Bouches-du-Rhône (13)</a></td></tr>
  <tr><th>Arrondissements:</th><td>Marseille</td></tr>
  <tr><th>Cantons:</th><td>Plusieurs</td></tr>
  <tr><th>Codes postaux:</th><td>13001 - 13016</td></tr>
  <tr><th>Site web:</th><td><a href="#">http://www.portmarsal.fr/</a></td></tr>
</table>

<h2 class="section-title abs" style="left:204px;top:414px">Informations touristiques</h2>
<p class="tourism">Marseille n'est pas seulement la ville la plus âgée de la France - à cause de son important port commercial, elle est aussi appelée « la porte au monde ». Fondée en 600 avant J.- C. par des marins Grecs de Phocée, Marseille est le premier port de la France. Marseille est le siège d'un archevêque, ville d'université et capitale de départements Bouches-du-Rhône. La ville doit son expansion et prospérité à son port, qui est un lieu de transbordement important pour des marchandises destinées pour l'Afrique du Nord et l'Asie. Spécialement le pétrole occupe une position éminente.</p>
<a class="more" href="#">En savoir plus <svg width="6" height="5" viewBox="0 0 6 5"><path d="M0 0h6L3 5z" fill="#2d5f95"/></svg></a>

<aside>
  <div class="widget-upload">Envoyez vos photos<br>de Marseille
    <svg width="16" height="11" viewBox="0 0 16 11" style="vertical-align:-1px;margin-left:4px"><path d="M4 11a3.5 3.5 0 0 1-.4-7A4.5 4.5 0 0 1 12.3 4 3.5 3.5 0 0 1 12 11z" fill="#fff"/><path d="M8 4l-2.5 3h1.7v3h1.6V7h1.7z" fill="#2f6090"/></svg>
  </div>
  <div class="widget-head" style="top:299px">Météo</div>
  <div class="widget-body" style="top:327px;height:71px">
    <svg class="abs" style="left:19px;top:10px" width="50" height="50" viewBox="0 0 50 50">
      <circle cx="25" cy="25" r="13" fill="var(--sun)"/>
      <g fill="var(--sun)"><path d="M25 0l4 7h-8z"/><path d="M25 50l4-7h-8z"/><path d="M0 25l7-4v8z"/><path d="M50 25l-7-4v8z"/><path d="M7 7l8 2-6 6z"/><path d="M43 7l-2 8-6-6z"/><path d="M7 43l2-8 6 6z"/><path d="M43 43l-8-2 6-6z"/></g>
    </svg>
    <div class="abs" style="left:95px;top:21px">Temp: <b>24°C</b></div>
    <div class="abs" style="left:87px;top:40px">Vent: <b>36km/h</b></div>
  </div>
  <div class="widget-head" style="top:419px">Gratuit!</div>
  <div class="widget-body" style="top:448px;height:38px;padding:5px 13px;line-height:14px">Widget météo pour<br>votre site web</div>
</aside>

<section class="lower">
  <h2 class="section-title abs" style="left:13px;top:14px">Villes aux alentours de Marseille</h2>
  <div class="nearby">
    <a href="#">Fontvieille</a><a href="#">Allauch</a><a href="#">Plan-de-Cuques</a><a href="#">La Penne-sur-Huveaune</a><a href="#">Septèmes-les-Vallons</a><a href="#">Simiane-Collongue</a><a href="#">Carnoux-en-Provence</a><a href="#">Aubagne</a><a href="#">Les Pennes-Mirabeau</a><a href="#">Le Rove</a><a href="#">Cassis</a>
    <span class="d">6.99km</span><span class="d">7.69km</span><span class="d">7.74km</span><span class="d">9.62km</span><span class="d">11.43km</span><span class="d">13.25km</span><span class="d">13.35km</span><span class="d">13.61km</span><span class="d">13.79km</span><span class="d">14.21km</span><span class="d">14.22km</span>
    <a href="#">Cabriès</a><a href="#">Cadolive</a><a href="#">Mimet</a><a href="#">Saint-Savournin</a><a href="#">Bouc-Bel-Air</a><a href="#">Gignac-la-Nerthe</a><a href="#">Roquevaire</a><a href="#">Ensuès-la-Redonne</a><a href="#">Peypin</a><a href="#">Gardanne</a><span></span>
    <span class="d">14.88km</span><span class="d">15.25km</span><span class="d">15.28km</span><span class="d">15.48km</span><span class="d">16.72km</span><span class="d">16.89km</span><span class="d">17.10km</span><span class="d">17.10km</span><span class="d">17.47km</span><span class="d">17.52km</span><span></span>
  </div>
  <div class="lower-divider"></div>
  <h2 class="section-title abs" style="left:318px;top:14px">Photos de Marseille</h2>
  <div class="photos" role="img" aria-label="Vignettes de photos de Marseille">
    <div></div><div></div><div></div><div></div><div></div><div></div><div></div><div></div><div></div><div></div><div></div><div></div>
  </div>
</section>

<footer class="site-footer">
  <div class="footer-brand"><span></span>ormavue</div>
  <div class="abs" style="left:51px;top:63px">© 2004-2013 ormavue.com</div>
  <div class="footer-links">
    <a href="#" style="left:51px;top:93px;text-decoration:underline;font-weight:600">Home</a>
    <a href="#" style="left:51px;top:108px">Archives</a>
    <a href="#" style="left:51px;top:123px">About</a>
    <a href="#" style="left:51px;top:138px">Contact</a>
  </div>
  <div class="foot-title" style="left:204px">LES PLUS BELLES VILLES</div>
  <div class="city-links" style="font-weight:600">
    <a href="#" style="left:204px;top:57px">Strasbourg</a>
    <a href="#" style="left:204px;top:78px;text-decoration:underline">Marseille</a>
    <a href="#" style="left:204px;top:99px">Bormes-Les-Mimosas</a>
    <a href="#" style="left:204px;top:121px">Paris</a>
    <a href="#" style="left:204px;top:142px">Lyon</a>
  </div>
  <div class="foot-title" style="left:356px">LATEST NEWS</div>
  <div class="news">
    <div style="font-weight:600">Karim Valadeh conteste l'exclusion de son allié en Iran</div>
    <div style="font-size:7px;font-style:italic;font-weight:600;margin-top:8px">May 22, 2013 • 1 Comment</div>
    <div style="margin-top:9px">par Soraya Nadiri DUBAI (Agence Lumen) - Le président iranien, Karim Valadeh, a</div>
    <div style="font-style:italic;font-weight:600;margin-top:9px">Savoir plus...</div>
  </div>
  <div class="foot-title" style="left:508px">PHOTOS</div>
  <div class="foot-photos">
    <div role="img" aria-label="Photo d'un bâtiment" style="background:#8a9aab"></div>
    <div role="img" aria-label="Photo d'une fleur rouge" style="background:#c8506a"></div>
    <div role="img" aria-label="Photo de cabanes de plage colorées" style="background:#c9773a"></div>
    <div role="img" aria-label="Photo de pierres" style="background:#8a7a68"></div>
    <div role="img" aria-label="Photo d'un port" style="background:#6f8eb0"></div>
    <div role="img" aria-label="Photo de sculptures" style="background:#7d6a3a"></div>
  </div>
</footer>

</body>
</html>
```